Halvorsen Partners Business Card

Halvorsen Partners Civil Construction
Marcus Halvorsen
CEO
727-518-6094
Marcus@HalvorsenSiteworks.example
www.HalvorsenSiteworks.example
Site Development
Utility Construction
Excavation
40876 County Lane 19
Land O' Lakes, FL 34638

Target Market(s)

Construction and government

Industry/Entity Type

Business

Contact Information for Business Card

I want an unique design that make a statement

Number of Pages Required

1 page

Font styles to use

Colors

Designer to choose colors to be used in the design.

Requirements
Must have
• unique design, feel free to modify or change the color of my logo.
Nice to have
• extra design features like spot UV, foil accents, color edges, unique paper, or any thing that would make my card pop.
• I like the feel of the image that I attached

```html
<!DOCTYPE html>
<html lang="en">
<head>
<meta charset="utf-8">
<title>Halvorsen Partners Business Card</title>
<link rel="stylesheet" href="https://fonts.googleapis.com/css2?family=Open+Sans:wght@400;600;700&display=swap">
<style>
  :root {
    --backdrop: #e6e4e1;
    --card-dark: #1d1e20;
    --card-dark-edge: #2a2b2e;
    --card-light: #f3f3f2;
    --brand-blue: #2b4f9e;
    --brand-navy: #1f3f8a;
    --slate: #7a7c80;
    --ink: #3c3d40;
    --rule: #5a5c60;
  }
  * { box-sizing: border-box; margin: 0; padding: 0; }
  html, body {
    width: 1200px; height: 723px; overflow: hidden;
    background: var(--backdrop);
    font-family: "Open Sans", Arial, sans-serif;
  }
  .canvas {
    position: relative; width: 1200px; height: 723px;
    display: flex; align-items: center; justify-content: center; gap: 40px;
  }
  .card {
    position: relative; width: 540px; height: 309px;
    border-radius: 4px; overflow: hidden;
    box-shadow: 0 10px 28px rgba(0,0,0,0.22);
  }

  /* Front */
  .card--front {
    background: linear-gradient(135deg, var(--card-dark-edge) 0%, var(--card-dark) 60%);
    color: var(--slate);
  }
  .brand {
    position: absolute; left: 38px; top: 92px;
    display: flex; align-items: center; gap: 20px;
  }
  .brand__square {
    width: 46px; height: 46px; border: 5px solid var(--brand-blue); flex: none;
  }
  .brand__divider {
    width: 1px; height: 78px; background: var(--rule); flex: none;
  }
  .brand__text { display: flex; flex-direction: column; gap: 6px; }
  .brand__name {
    font-weight: 700; font-size: 31px; line-height: 1; letter-spacing: 0.5px;
    color: var(--brand-blue); text-transform: uppercase;
  }
  .brand__tagline {
    font-weight: 400; font-size: 15px; letter-spacing: 6.4px;
    color: var(--slate); text-transform: uppercase;
  }
  .services {
    position: absolute; right: 38px; bottom: 36px; width: 250px;
    border-top: 1px solid var(--rule); padding-top: 12px;
    text-align: right; font-size: 11px; line-height: 1.7; color: var(--slate);
  }

  /* Back */
  .card--back {
    background: var(--card-light);
    border-left: 8px solid var(--brand-blue);
  }
  .person { position: absolute; left: 40px; top: 52px; }
  .person__name {
    font-weight: 700; font-size: 32px; line-height: 1; color: var(--brand-navy);
  }
  .person__title {
    margin-top: 6px; font-size: 20px; letter-spacing: 9px; color: var(--slate);
  }
  .contacts {
    position: absolute; right: 36px; bottom: 38px;
    list-style: none; display: flex; flex-direction: column; gap: 12px;
  }
  .contacts__item {
    display: flex; align-items: center; gap: 12px;
    font-size: 14px; color: var(--ink);
  }
  .contacts__icon { width: 20px; height: 20px; flex: none; fill: var(--ink); }
</style>
</head>
<body>
<main class="canvas">

  <section class="card card--front" aria-label="Card front">
    <div class="brand">
      <span class="brand__square" aria-hidden="true"></span>
      <span class="brand__divider" aria-hidden="true"></span>
      <div class="brand__text">
        <span class="brand__name">Halvorsen Partners</span>
        <span class="brand__tagline">Civil Construction</span>
      </div>
    </div>
    <div class="services">
      Site Development<br>
      Utility Construction<br>
      Excavation
    </div>
  </section>

  <section class="card card--back" aria-label="Card back">
    <div class="person">
      <h1 class="person__name">Marcus Halvorsen</h1>
      <p class="person__title">CEO</p>
    </div>
    <ul class="contacts">
      <li class="contacts__item">
        <svg class="contacts__icon" viewBox="0 0 24 24" aria-hidden="true">
          <path d="M6.6 10.8c1.4 2.8 3.8 5.1 6.6 6.6l2.2-2.2c.3-.3.7-.4 1-.2 1.1.4 2.3.6 3.6.6.6 0 1 .4 1 1V20c0 .6-.4 1-1 1C10.6 21 3 13.4 3 4c0-.6.4-1 1-1h3.5c.6 0 1 .4 1 1 0 1.3.2 2.5.6 3.6.1.3 0 .7-.2 1l-2.3 2.2z"/>
        </svg>
        <span>727-518-6094</span>
      </li>
      <li class="contacts__item">
        <svg class="contacts__icon" viewBox="0 0 24 24" aria-hidden="true">
          <path d="M3 5h18a1 1 0 0 1 1 1v12a1 1 0 0 1-1 1H3a1 1 0 0 1-1-1V6a1 1 0 0 1 1-1zm1 2.2V17h16V7.2l-8 5.3-8-5.3zM5.5 7l6.5 4.3L18.5 7h-13z"/>
        </svg>
        <span>Marcus@HalvorsenSiteworks.example</span>
      </li>
      <li class="contacts__item">
        <svg class="contacts__icon" viewBox="0 0 24 24" aria-hidden="true">
          <path d="M12 2a10 10 0 1 0 0 20 10 10 0 0 0 0-20zm6.9 9h-3c-.1-2.2-.6-4.2-1.4-5.7A8 8 0 0 1 18.9 11zM12 4c.9 1.2 1.8 3.6 1.9 7h-3.8c.1-3.4 1-5.8 1.9-7zM9.5 5.3C8.7 6.8 8.2 8.8 8.1 11h-3a8 8 0 0 1 4.4-5.7zM5.1 13h3c.1 2.2.6 4.2 1.4 5.7A8 8 0 0 1 5.1 13zm6.9 7c-.9-1.2-1.8-3.6-1.9-7h3.8c-.1 3.4-1 5.8-1.9 7zm2.5-1.3c.8-1.5 1.3-3.5 1.4-5.7h3a8 8 0 0 1-4.4 5.7z"/>
        </svg>
        <span>www.HalvorsenSiteworks.example</span>
      </li>
    </ul>
  </section>

</main>
</body>
</html>
```